Business Cards and Stationary Design for Landscaping Company
Merriweather's Yard Crafting
Business Cards and Stationary Design for Landscaping Company - Home and Garden
Creative Brief
Simple
Dennis Carraway
President
PO Box 48213 Houston, TX 77241-4821
myc@merriweatheryard.com
www.merriweatheryard.com
Please make the YARD CRAFTING the same color as the light color swish

```html
<!DOCTYPE html>
<html lang="en">
<head>
<meta charset="utf-8">
<title>Merriweather's Yard Crafting – Stationery</title>
<link href="https://fonts.googleapis.com/css2?family=Open+Sans:wght@400;600;700&display=swap" rel="stylesheet">
<style>
:root{
  --bg:#e9eaea;
  --paper:#ffffff;
  --green-dark:#3d7a2a;
  --green-light:#8dbf42;
  --text:#6a6a6a;
  --shadow:0 2px 6px rgba(0,0,0,.12);
}
*{margin:0;padding:0;box-sizing:border-box}
html,body{width:1200px;height:936px;overflow:hidden;background:var(--bg)}
body{position:relative;font-family:"Open Sans",Arial,sans-serif;color:var(--text)}
.sheet{position:absolute;background:var(--paper);box-shadow:var(--shadow);overflow:hidden}
.band{position:absolute;left:0;right:0;background:linear-gradient(var(--green-light),var(--green-dark));color:#fff;text-align:center;font-weight:600;letter-spacing:.5px;white-space:nowrap}

/* brand name: one colour, one weight, small square beside */
.brand{display:flex;align-items:center;gap:6px;white-space:nowrap}
.brand .square{flex:none;background:var(--green-dark)}
.brand .name{font-family:"Open Sans",Arial,sans-serif;font-weight:700;color:var(--green-dark);line-height:1.15}

/* letterhead */
.letterhead{left:178px;top:51px;width:393px;height:571px}
.letterhead .brand{position:absolute;left:38px;top:34px}
.letterhead .square{width:12px;height:12px}
.letterhead .name{font-size:7px}
.letterhead .contact{position:absolute;right:30px;top:30px;text-align:right;font-size:5.5px;line-height:1.5}
.letterhead .body{position:absolute;left:38px;right:38px;top:128px;font-size:5.4px;line-height:1.55}
.letterhead .body p{margin-bottom:9px}
.signature{width:30px;height:12px;background:#d8d8d8;margin-bottom:6px}
.letterhead .band{bottom:9px;height:20px;font-size:7.5px;line-height:20px}

/* folder */
.folder{left:637px;top:46px;width:423px;height:576px}
.folder .brand{position:absolute;left:0;right:0;top:238px;justify-content:center;gap:12px}
.folder .square{width:26px;height:26px}
.folder .name{font-size:22px}
.folder .band{bottom:9px;height:20px;font-size:8px;line-height:20px}

/* cards */
.card{left:41px;width:192px}
.card-front{top:647px;height:124px}
.card-back{top:781px;height:97px}
.card-front .brand{position:absolute;left:12px;top:16px;gap:4px}
.card-front .square{width:8px;height:8px}
.card-front .name{font-size:6px}
.card-front .info{position:absolute;left:12px;top:52px;font-size:4.6px;line-height:1.5}
.card-front .who{position:absolute;right:14px;top:52px;text-align:right;font-size:5px;line-height:1.45}
.card-front .band{bottom:14px;height:5px}
.card-back .band{bottom:18px;height:14px;font-size:6.5px;line-height:14px}

/* envelopes */
.envelope-front{left:264px;top:672px;width:416px;height:206px}
.envelope-front .brand{position:absolute;left:34px;top:26px;gap:5px}
.envelope-front .square{width:10px;height:10px}
.envelope-front .name{font-size:7.5px}
.envelope-front .band{bottom:12px;height:14px;font-size:7px;line-height:14px}
.envelope-back{left:736px;top:672px;width:428px;height:206px}
.envelope-back svg{position:absolute;left:0;top:0}
.envelope-back .band{bottom:60px;height:14px;font-size:7px;line-height:14px}
</style>
</head>
<body>

<section class="sheet letterhead">
  <div class="brand">
    <span class="square"></span>
    <span class="name">Merriweather's<br>Yard Crafting</span>
  </div>
  <div class="contact">
    PO Box 48213<br>Houston, TX 77241-4821<br><br>713-555-0148<br>myc@merriweatheryard.com
  </div>
  <div class="body">
    <p>March 12, 2024<br><br>Dear Client,<br>Oak Street Office, Houston, Texas</p>
    <p>Thank you for choosing our team to care for your outdoor spaces this season. We are pleased to confirm that our crew will begin the spring cleanup next week, followed by fresh mulch, edging and a full review of your irrigation zones. Our foreman will call ahead to set a convenient arrival time.</p>
    <p>Throughout the year we will keep your lawn healthy with regular mowing, seasonal feeding and careful pruning of shrubs and young trees. Any new planting beds or stone borders you would like to add can be planned together during our next visit.</p>
    <p>Should you have any questions about the schedule or the estimate enclosed with this letter, please reach out by phone or email at any time. We look forward to a long and green partnership.</p>
    <p>Best Regards,</p>
    <div class="signature" role="img" aria-label="Handwritten signature"></div>
    <p>Dennis Carraway<br>President<br>Merriweather's Yard Crafting, Houston, Texas</p>
  </div>
  <div class="band">www.merriweatheryard.com</div>
</section>

<section class="sheet folder">
  <div class="brand">
    <span class="square"></span>
    <span class="name">Merriweather's Yard Crafting</span>
  </div>
  <div class="band">www.merriweatheryard.com</div>
</section>

<section class="sheet card card-front">
  <div class="brand">
    <span class="square"></span>
    <span class="name">Merriweather's Yard Crafting</span>
  </div>
  <div class="info">PO Box 48213<br>Houston, TX 77241-4821<br>713-555-0148<br>myc@merriweatheryard.com</div>
  <div class="who">Dennis Carraway<br>President</div>
  <div class="band"></div>
</section>

<section class="sheet card card-back">
  <div class="band">www.merriweatheryard.com</div>
</section>

<section class="sheet envelope-front">
  <div class="brand">
    <span class="square"></span>
    <span class="name">Merriweather's<br>Yard Crafting</span>
  </div>
  <div class="band">www.merriweatheryard.com</div>
</section>

<section class="sheet envelope-back">
  <svg width="428" height="206" viewBox="0 0 428 206" aria-hidden="true">
    <polyline points="0,0 214,92 428,0" fill="none" stroke="#d6d6d6" stroke-width="1"/>
    <line x1="0" y1="206" x2="175" y2="100" stroke="#ececec" stroke-width="1"/>
    <line x1="428" y1="206" x2="253" y2="100" stroke="#ececec" stroke-width="1"/>
  </svg>
  <div class="band">www.merriweatheryard.com</div>
</section>

</body>
</html>
```